Tallyleaf Web Design

Create Website Design for Tallyleaf. Tallyleaf is online application for collaboration team work system (task list management). More concept design for this project please find attach file ("tallyleaf website concept.pdf") . But my concept is just describe minimal features not bind design

For tallyleaf logo, i had already attach files. But i had not decided what color i chose, so it's okay if you suggest logo color for your suitable website design.
Updates

Dear All Designer,

I like brisk carousel (http://quorvanlabs.example/brisk-carousel/),
may be your concept design can adjust with this concept.
but don't worry about script for brisk carousel, my team will be handle
You just make website design to suitable with brisk carousel

but if you had own website design concept are welcome

thanks

Target Market(s)

Business Company

Industry/Entity Type

Management

```html
<!DOCTYPE html>
<html lang="en">
<head>
<meta charset="utf-8">
<title>Tallyleaf – Online Collaboration Team Work</title>
<link rel="stylesheet" href="https://fonts.googleapis.com/css2?family=Open+Sans:wght@300;400;600;700&display=swap">
<style>
  :root{
    --nav-bg:#26463c;
    --hero-top:#1c3a31;
    --hero-bottom:#163028;
    --page-bg:#ebebeb;
    --nav-text:#e4eee9;
    --head-light:#86cdb6;
    --head-bold:#d9f0e8;
    --brand:#8cc63f;
    --section-title:#1f6b55;
    --body-text:#555;
    --rule:#d4d4d4;
    --frame:#c9cbca;
    --app-blue:#1d3f7a;
    --app-link:#1a3fb8;
    --badge-task:#e05050;
    --badge-comment:#2fa83a;
    --badge-done:#9a9a9a;
  }
  *{margin:0;padding:0;box-sizing:border-box}
  html,body{width:1200px;height:1032px;overflow:hidden}
  body{font-family:"Open Sans",sans-serif;background:var(--page-bg);position:relative}
  .hero-band{position:absolute;left:0;top:0;width:1200px;height:350px;
    background:linear-gradient(180deg,var(--hero-top),var(--hero-bottom))}
  .top-nav{position:absolute;left:0;top:0;width:1200px;height:45px;background:var(--nav-bg)}
  .top-nav ul{list-style:none;position:absolute;left:170px;top:13px;display:flex;gap:25px}
  .top-nav a{color:var(--nav-text);text-decoration:none;font-size:13px}
  .top-nav a.sign-in{font-weight:700}
  .phone{position:absolute;right:172px;top:12px;color:var(--nav-text);font-size:14px;display:flex;align-items:center;gap:8px}
  .brand{position:absolute;left:0;width:1200px;top:62px;text-align:center;
    font-size:58px;font-weight:600;color:var(--brand);letter-spacing:-1px}
  .showcase{position:absolute;left:171px;top:154px;width:858px;height:520px;border-radius:8px;
    background:linear-gradient(180deg,rgba(255,255,255,.04),rgba(230,232,231,.5) 60%,rgba(235,235,235,0))}
  .tagline{position:absolute;left:0;width:1200px;top:176px;text-align:center;font-size:27px;
    font-weight:300;color:var(--head-light)}
  .tagline b{font-weight:700;color:var(--head-bold)}

  /* side slides */
  .slide-side{position:absolute;top:252px;width:260px;height:363px;border:6px solid var(--frame);
    border-radius:4px;overflow:hidden}
  .slide-side.left{left:202px;background:#1f2324}
  .slide-side.right{left:738px;background:#1f3149}
  .stat-top{position:absolute;left:0;top:10px;width:70px;height:34px;background:#2a2a2a;color:#fff;font-size:14px;padding:9px 0 0 6px}
  .stat-top small{color:#c33;font-size:6px;margin-right:2px}
  .section-item{position:absolute;left:0;width:80px;height:47px;padding:6px 0 0 12px;color:#fff;border-top:1px solid #3a3a3a;background:#2b2f31}
  .section-item.active{background:#2c4766}
  .section-item b{display:block;font-size:12px;font-weight:700}
  .section-item span{font-size:10px;color:#9aa}
  .calc{position:absolute;left:188px;width:58px;height:19px;background:#3b4d63;border:1px solid #5c6f86;color:#fff;font-size:11px;text-align:center;line-height:17px}
  .calc.blank{background:#2d3d52;border-color:#3f5068}
  .calc-table{position:absolute;left:188px;top:311px;width:70px;border-collapse:collapse;font-family:monospace;font-size:7px;background:#fff}
  .calc-table th{background:#1aa3a8;color:#fff;padding:1px;font-weight:400}
  .calc-table td{padding:6px 2px;border-top:1px solid #ddd}

  /* main slide: app screen */
  .slide-main{position:absolute;left:277px;top:227px;width:646px;height:430px;border:6px solid var(--frame);
    border-radius:4px;background:#e7eaef;overflow:hidden;box-shadow:0 6px 14px rgba(0,0,0,.25);font-size:6.5px;color:#444}
  .app-bar{height:16px;background:#111;display:flex;align-items:flex-end;padding-left:10px;gap:2px;position:relative}
  .app-bar span{background:#555;color:#ddd;padding:2px 7px;font-size:5.5px;border-radius:2px 2px 0 0}
  .app-bar span.on{background:#2d5ba8;color:#fff}
  .app-bar .meta{position:absolute;right:4px;top:4px;background:none;color:#ddd;padding:0}
  .app-head{height:44px;background:linear-gradient(180deg,#1f4488,#173670);position:relative}
  .app-title{position:absolute;left:18px;top:8px;color:#fff;font-size:12px}
  .app-title small{font-size:8px;color:#d5def0}
  .app-choose{position:absolute;right:4px;top:11px;color:#f1c40f;font-size:7px;text-decoration:underline}
  .app-tabs{position:absolute;left:164px;bottom:0;display:flex;gap:2px}
  .app-tabs span{background:#e6e9ee;color:#333;padding:2px 4px;font-size:5.5px}
  .app-tabs span.on{background:#fff;font-weight:700}
  .app-side{position:absolute;left:6px;top:66px;width:148px;height:360px;background:#fff;border:1px solid #ccd;padding:8px}
  .app-brand{font-size:17px;font-weight:600;color:var(--brand);padding-left:4px}
  .app-desc{margin-top:8px;background:#eef1f5;padding:4px 6px;font-size:6.5px;line-height:7px}
  .app-side h4{font-size:7px;margin:9px 0 5px;font-weight:700}
  .app-side ul{list-style:none}
  .app-side li{margin:0 0 7px 8px;color:#222;text-decoration:underline;font-size:6.5px}
  .crew-bar{background:#cfdcf3;padding:2px 4px;font-weight:700;font-size:6px;margin-top:4px}
  .member{margin-top:6px;border:1px solid #ddd;padding:5px;position:relative;height:74px;line-height:8px}
  .member b{font-weight:400;font-size:7.5px}
  .member .photo{position:absolute;right:6px;top:6px;width:28px;height:30px;background:linear-gradient(#c9a98c,#7a6a5e)}
  .member .mail{color:var(--app-link);text-decoration:underline}
  .app-main{position:absolute;left:160px;top:66px;width:480px;height:360px;background:#fff;border:1px solid #ccd}
  .ov-head{height:20px;background:linear-gradient(#fff,#e8ecf2);padding:4px 6px;font-size:9px;font-weight:700;color:#223;position:relative}
  .ov-btns{position:absolute;right:0;top:5px;display:flex;gap:3px}
  .ov-btns span{border:1px solid #bbc;border-radius:6px;padding:1px 4px;font-size:5.5px;font-weight:400;background:#fff}
  .ov-tabs{display:flex;gap:12px;padding:6px 6px 0;border-bottom:1px solid #ccd;height:20px;font-size:5.8px}
  .ov-tabs .on{font-weight:700;border:1px solid #ccd;border-bottom:none;padding:2px 5px;background:#fff}
  .ov-tabs span{padding:2px 0}
  .day{margin:8px 4px 2px;background:#dfe2e6;padding:2px 6px;font-weight:700;font-size:7px}
  .day mark{background:#f4c20d;padding:0 3px}
  .row{display:flex;align-items:center;padding:0 4px 0 6px;height:17px;border-bottom:1px solid #eee;position:relative}
  .row.tall{height:22px}
  .badge{width:22px;text-align:center;color:#fff;font-size:4.5px;padding:1px 0;margin-right:6px;flex:none;border-radius:1px;background:var(--badge-task)}
  .badge.c{background:var(--badge-comment);width:30px;margin-left:-8px}
  .badge.d{background:var(--badge-done)}
  .row .txt{width:340px;font-size:5.6px;line-height:6.5px}
  .row .txt u{color:var(--app-link)}
  .row .txt s{color:#888}
  .row .when{position:absolute;right:2px;font-size:5px;color:#999}
  .row.y{height:14px}

  .feature{position:absolute;top:722px;width:232px}
  .feature h2{font-size:19px;font-weight:600;color:var(--section-title);margin-bottom:12px;white-space:nowrap}
  .feature .thumb{width:231px;height:81px;border:1px solid #ccc}
  .feature p{margin-top:16px;font-size:11px;line-height:20.6px;color:var(--body-text);text-align:justify;letter-spacing:-0.15px;width:232px}
  .f1{left:208px}.f2{left:485px}.f3{left:760px}
  .thumb.app{background:linear-gradient(180deg,#e8ebef,#c9d0d8)}
  .thumb.sync{background:radial-gradient(ellipse at center,#3a6e9a,#0b1a2a 70%)}
  .thumb.report{background:linear-gradient(135deg,#f2f2f2,#b9c4d2)}
  .footer-rule{position:absolute;left:171px;top:967px;width:858px;border-top:1px solid var(--rule)}
  .footer-nav{position:absolute;left:208px;top:992px;list-style:none;display:flex;gap:16px}
  .footer-nav a{font-size:11px;color:#666;text-decoration:none}
  .copyright{position:absolute;right:208px;top:992px;font-size:11px;color:#666}
</style>
</head>
<body>
  <div class="hero-band"></div>
  <nav class="top-nav">
    <ul>
      <li><a href="#">Features</a></li>
      <li><a href="#">Pricing</a></li>
      <li><a href="#">Security</a></li>
      <li><a href="#">FAQ</a></li>
      <li><a href="#">Projects</a></li>
      <li><a href="#" class="sign-in">Sign In</a></li>
    </ul>
    <div class="phone">
      <svg width="10" height="14" viewBox="0 0 10 14"><rect x="0.5" y="0.5" width="9" height="13" rx="1.5" fill="none" stroke="#9fb7ad"/><rect x="2" y="2" width="6" height="5" fill="#9fb7ad"/><rect x="2" y="9" width="6" height="3" fill="#9fb7ad"/></svg>
      310-555-0187
    </div>
  </nav>

  <div class="brand">tallyleaf</div>

  <div class="showcase"></div>
  <h1 class="tagline">Customize <b>Online</b> Collaboration <b>Team Work</b></h1>

  <div class="slide-side left">
    <div class="stat-top"><small>Epsilon</small>38,47</div>
    <div class="section-item" style="top:52px"><b>odsek 1</b><span>merska tocka</span></div>
    <div class="section-item" style="top:100px"><b>odsek 2</b><span>merska tocka</span></div>
    <div class="section-item active" style="top:148px"><b>odsek 3</b><span>merska tocka</span></div>
  </div>

  <div class="slide-side right">
    <div class="calc" style="top:10px">90</div>
    <div class="calc" style="top:34px">115</div>
    <div class="calc" style="top:58px">Undo</div>
    <div class="calc" style="top:82px">-</div>
    <div class="calc blank" style="top:124px"></div>
    <div class="calc blank" style="top:148px"></div>
    <div class="calc blank" style="top:172px"></div>
    <div class="calc blank" style="top:196px"></div>
    <table class="calc-table">
      <tr><th>g(L)</th><th>t·avg</th></tr>
      <tr><td>0,00</td><td>5,33</td></tr>
      <tr><td>5,33</td><td></td></tr>
      <tr><td>0,00</td><td>3,67</td></tr>
      <tr><td>3,67</td><td></td></tr>
      <tr><td>0,00</td><td></td></tr>
    </table>
  </div>

  <div class="slide-main">
    <div class="app-bar">
      <span>Dashboard</span><span>All Items</span><span class="on">Project View</span><span>Calendar</span>
      <span class="meta">Settings &nbsp; Jan 17 2009</span>
    </div>
    <div class="app-head">
      <div class="app-title">Crewdesk Project Manager <small>» Northfield Crew</small></div>
      <div class="app-choose">CHOOSE ANOTHER</div>
      <div class="app-tabs">
        <span class="on">Overview</span><span>Tasks</span><span>Milestones</span><span>Messages</span><span>Files</span><span>Time</span><span>Notebook</span><span>Risk Register</span><span>Permissions</span>
      </div>
    </div>

    <aside class="app-side">
      <div class="app-brand">tallyleaf</div>
      <div class="app-desc">Crewdesk Project Manager - Web based project collaboration tool</div>
      <h4>Project options</h4>
      <ul>
        <li>Project Permissions</li><li>Project Roles</li><li>Project settings</li><li>Copy this Project</li><li>Unstar this project</li>
      </ul>
      <h4>Project members</h4>
      <div style="color:var(--app-link);font-size:5.5px;text-decoration:underline">Add more people to this project ...</div>
      <div class="crew-bar">Northfield Crew</div>
      <div class="member">
        <div class="photo" role="img" aria-label="Member photo"></div>
        <b>Aaron Pell</b><br>Application Developer<br><span class="mail">aaron@northfield-crew.example</span><br>Phone: 555 01 200 4418<br>Mobile: 555012004419<br>Administrator
      </div>
      <div class="member">
        <div class="photo" role="img" aria-label="Member photo"></div>
        <b>Mira Lonsdale</b><br>Designer/Front End<br>Developer<br><span class="mail">mira@northfield-crew.example</span>
      </div>
    </aside>

    <section class="app-main">
      <div class="ov-head">Project Overview
        <div class="ov-btns"><span>+ Add Task List</span><span>+ Add Milestone</span><span>+ Add Message</span><span>Print</span></div>
      </div>
      <div class="ov-tabs"><span class="on">Latest Activity</span><span>Todays Tasks</span><span>Upcoming Tasks</span></div>

      <div class="day"><mark>Today</mark></div>
      <div class="row"><span class="badge">Task</span><span class="txt"><u>Include notes etc in PDF download of Notebooks</u> (List: <u>Main Task List</u>)</span><span class="when">Edited 14 minutes ago</span></div>
      <div class="row"><span class="badge d">Task</span><span class="txt"><s>Users : Ability to move users between companies (List: Must Do - ASAP)</s></span><span class="when">Completed 40 minutes ago</span></div>
      <div class="row tall"><span class="badge c">Comment</span><span class="txt"><u>You can now move users between companies if you are an Administrator. Click..</u> (Task: Users : Ability to move users between companies)</span><span class="when">Written 40 minutes ago</span></div>
      <div class="row"><span class="badge">Task</span><span class="txt"><u>Activity Log : When a message is deleted it needs to be deleted from the activ..</u> (List: <u>Minor Bug Fixes</u>)</span><span class="when">Edited about 2 hours ago</span></div>
      <div class="row tall"><span class="badge c">Comment</span><span class="txt"><u>Ok, but the link needs to be removed so people cant click it when missing..</u> (Task: Activity Log : When a message is deleted it need..)</span><span class="when">Written about 4 hours ago</span></div>
      <div class="row tall"><span class="badge c">Comment</span><span class="txt"><u>Yeah it's easy but does it make sense. With tasks we dont pretend the task ne..</u> (Task: Activity Log : When a message is deleted it need..)</span><span class="when">Written about 4 hours ago</span></div>

      <div class="day">Yesterday</div>
      <div class="row y"><span class="badge">Task</span><span class="txt"><u>File icon on Dashboard. The Votes have it.... it looks nice.</u> (List: <u>Suggestions (important)</u>)</span><span class="when">Created and assigned by Aaron</span></div>
      <div class="row y"><span class="badge c">Comment</span><span class="txt"><u>This was one of the things for Harbor Outlet.</u> (Task: Activity Log : When a message is deleted it need..)</span><span class="when">Written</span></div>
      <div class="row y"><span class="badge">Task</span><span class="txt"><u>Activity Log : When a message is deleted it needs to be deleted from the activ..</u> (List: <u>Minor Bug Fixes</u>)</span><span class="when">Created and assigned by Aaron</span></div>
      <div class="row y"><span class="badge c">Comment</span><span class="txt"><u>Cool.</u> (Task: Seems to be a problem with message Activity log)</span><span class="when">Written</span></div>
      <div class="row y"><span class="badge c">Comment</span><span class="txt"><u>Sorry. I fixed this a while back and forgot to notify you.</u> (Task: Major issue with deleting some messages)</span><span class="when">Written</span></div>
      <div class="row y"><span class="badge d">Task List</span><span class="txt"><s>Major Bug Fixes</s></span><span class="when">Completed</span></div>
      <div class="row y"><span class="badge d">Task</span><span class="txt"><s>Major issue with deleting some messages (List: Major Bug Fixes)</s></span><span class="when">Completed</span></div>
      <div class="row tall"><span class="badge c">Comment</span><span class="txt"><u>Hi, this is the last item on the Major Bug List - I cant recreate it. I was assigned by you..</u> (Task: Major issue with deleting some messages)</span><span class="when">Written</span></div>
      <div class="row y"><span class="badge d">Task</span><span class="txt"><s>Seems to be a problem with message Activity log (List: Major Bug Fixes)</s></span><span class="when">Completed</span></div>
    </section>
  </div>

  <section class="feature f1">
    <h2>Customize Application</h2>
    <div class="thumb app" role="img" aria-label="Application task list screenshot"></div>
    <p>On sait depuis longtemps que travailler avec du texte lisible et contenant du sens est source de distractions, et empêche de se concentrer sur la mise en page elle-même.</p>
  </section>
  <section class="feature f2">
    <h2>Synchronize all device</h2>
    <div class="thumb sync" role="img" aria-label="Illustration of devices connected to a cloud"></div>
    <p>On sait depuis longtemps que travailler avec du texte lisible et contenant du sens est source de distractions, et empêche de se concentrer sur la mise en page elle-même.</p>
  </section>
  <section class="feature f3">
    <h2>Report</h2>
    <div class="thumb report" role="img" aria-label="Photo of hands reviewing printed report charts"></div>
    <p>On sait depuis longtemps que travailler avec du texte lisible et contenant du sens est source de distractions, et empêche de se concentrer sur la mise en page elle-même.</p>
  </section>

  <div class="footer-rule"></div>
  <ul class="footer-nav">
    <li><a href="#">Features</a></li>
    <li><a href="#">Pricing</a></li>
    <li><a href="#">Security</a></li>
    <li><a href="#">FAQ</a></li>
    <li><a href="#">Projects</a></li>
  </ul>
  <div class="copyright">© Copyrights 2013 All rights Reserved</div>
</body>
</html>
```